BrightMold needs an insert advertising two dental laboratory products to go inside a Dental magazine.

We need an insert designed to go inside the Pacific Oral Health Guild bi-monthly magazine. The flyer is to promote two products ( a flexible partial denture and a bitesplint) to dentists. I will provide my company logo and write the script. The brochure needs to be professional looking and be effective.
Regards
Darren Whitcombe

Target Market(s)

Dentists

Industry/Entity Type

Dental

Font styles to use
Serif

Colors
3176b5

Requirements
Must have
• Contemporary, professional, clean lines, images.
Should not have
• Cluttered with too much information

```html
<!DOCTYPE html>
<html lang="en">
<head>
<meta charset="utf-8">
<title>BrightMold – Partial Dentures Insert</title>
<link href="https://fonts.googleapis.com/css2?family=Krona+One&family=Source+Sans+3:wght@400;600&display=swap" rel="stylesheet">
<style>
  :root {
    --brand-blue: #1a8fca;
    --brand-blue-deep: #1479b3;
    --heading-blue: #1d8ccb;
    --heading-navy: #0d2233;
    --ink: #1d1d1d;
    --backdrop: #a9a9ab;
    --page: #ffffff;
    --page-fade: #e9eaec;
    --rule: #c9cbce;
  }
  * { box-sizing: border-box; margin: 0; padding: 0; }
  html, body { width: 1200px; height: 1200px; overflow: hidden; }
  body { background: var(--backdrop); font-family: "Source Sans 3", Arial, sans-serif; }

  .insert {
    position: absolute; left: 184px; top: 20px;
    width: 832px; height: 1160px; overflow: hidden;
    background: linear-gradient(180deg, var(--page) 0%, var(--page) 55%, var(--page-fade) 100%);
  }
  .hero { position: absolute; left: 0; top: 0; }

  .copy { position: absolute; color: var(--ink); font-size: 13.6px; line-height: 16.6px; text-align: justify; }
  .copy p + p { margin-top: 9px; }
  .section-title {
    position: absolute; font-family: "Krona One", Arial, sans-serif;
    font-size: 13px; line-height: 21.5px; color: var(--heading-blue); font-weight: 400;
  }
  .panel-title { color: var(--heading-navy); }
  .panel-copy { color: #ffffff; }

  .info-panel {
    position: absolute; left: 426px; top: 440px; width: 378px; height: 538px;
    background: linear-gradient(180deg, var(--brand-blue) 0%, var(--brand-blue-deep) 100%);
  }

  .footer-divider { position: absolute; left: 411px; top: 1007px; width: 1px; height: 133px; background: var(--rule); }
  .brand {
    position: absolute; left: 72px; top: 1056px;
    font-family: "Source Sans 3", Arial, sans-serif; font-weight: 600;
    font-size: 32px; line-height: 1; color: var(--brand-blue-deep); letter-spacing: 1px;
  }

  .contact { position: absolute; left: 466px; top: 1012px; list-style: none; }
  .contact li { display: flex; align-items: center; gap: 11px; height: 22.5px; font-size: 13.6px; font-weight: 600; color: var(--ink); }
  .contact li.contact-name { font-family: "Krona One", Arial, sans-serif; font-weight: 400; font-size: 12.5px; height: 30px; }
  .contact svg { width: 19px; height: 19px; flex: none; }

  .base-rule { position: absolute; left: 0; top: 1140px; width: 832px; height: 4px; background: var(--rule); }
  .base-band { position: absolute; left: 0; top: 1146px; width: 832px; height: 14px; background: var(--brand-blue); }
</style>
</head>
<body>
<main class="insert">

  <svg class="hero" width="832" height="500" viewBox="0 0 832 500">
    <defs>
      <linearGradient id="heroTone" x1="0" y1="0" x2="1" y2="1">
        <stop offset="0" stop-color="#cfe3f2"/>
        <stop offset="0.45" stop-color="#f2d9dc"/>
        <stop offset="1" stop-color="#b9cfe6"/>
      </linearGradient>
      <radialGradient id="splintTone" cx="0.5" cy="0.45" r="0.6">
        <stop offset="0" stop-color="#e8d8a8"/>
        <stop offset="1" stop-color="#123c8c"/>
      </radialGradient>
      <radialGradient id="partialTone" cx="0.5" cy="0.5" r="0.6">
        <stop offset="0" stop-color="#f4e4e0"/>
        <stop offset="1" stop-color="#e6a9a4"/>
      </radialGradient>
    </defs>
    <path role="img" aria-label="Photo: smiling dentist showing a young girl how to brush teeth on a dental model while her mother watches"
          d="M0 0 H832 V262 C700 340 560 398 430 408 C280 418 110 382 0 300 Z" fill="url(#heroTone)"/>
    <path d="M832 262 C700 340 560 398 430 408 C280 418 110 382 0 300 V328 C110 412 280 448 426 446 V500 H804 V420 H832 Z" fill="#1a8fca"/>
    <path d="M0 328 C110 412 280 448 426 446 L426 470 C280 470 110 440 0 372 Z" fill="#eceef0"/>
    <circle cx="703" cy="317" r="92" fill="#ffffff"/>
    <circle role="img" aria-label="Photo: flexible pink partial denture" cx="703" cy="317" r="86" fill="url(#partialTone)"/>
    <circle cx="539" cy="400" r="89" fill="#ffffff"/>
    <circle role="img" aria-label="Photo: clear bite splint on a dental model" cx="539" cy="400" r="82" fill="url(#splintTone)"/>
  </svg>

  <div class="info-panel"></div>

  <h2 class="section-title" style="left:56px; top:468px;">Flexiline:</h2>
  <div class="copy" style="left:56px; top:494px; width:336px;">
    <p>Flexiline is a new generation flexible denture material, similar to Nylaform. It is ideal for smaller cases. Unlike Nylaform which is a nylon, Flexiline is made from polyolefin, which makes it very easy to adjust and polish. Flexiline is also very stain resistant. Your patients will appreciate the superior comfort of Flexiline, along with a natural translucency that allows the partial to virtually disappear in the mouth.</p>
  </div>

  <h2 class="section-title" style="left:56px; top:637px;">Rigiform:</h2>
  <div class="copy" style="left:56px; top:663px; width:336px;">
    <p>Rigiform is a new semi-rigid thermoplastic that is ideal for larger partial denture cases. Its superior strength allows partials to be made a lot thinner and lighter than conventional acrylic dentures. Its flexibility allows undercuts to be engaged for retention, eliminating the need for unaesthetic metal clasps. Rigiform is practically unbreakable and its lack of processing shrinkage results in a perfect fit. Because Rigiform is not an acrylic, it is ideal for patients requiring an allergy free appliance.</p>
  </div>

  <h2 class="section-title" style="left:56px; top:824px;">Conventional Acrylic:</h2>
  <div class="copy" style="left:56px; top:850px; width:336px;">
    <p>For cases where you wish to supply a conventional acrylic denture, BrightMold offers a premium solution. All our partials are made from high impact, heat cured acrylic. Models are surveyed, blocked out, and dentures processed on a duplicate model. They are then carefully fitted to your original model, with the occlusion refined, before being sent back to your surgery. The result is a partial denture that fits first time, every time.</p>
  </div>

  <h2 class="section-title panel-title" style="left:445px; top:518px;">Who We Are:</h2>
  <div class="copy panel-copy" style="left:445px; top:546px; width:339px;">
    <p>I started BrightMold in 2016 looking to build a business around the changing technologies in dentistry. Prior to that I owned Northbay Dental Works, an Auckland based laboratory that grew from a one person lab to a 10 person lab before selling the business in 2013.</p>
    <p>BrightMold provides a complete removable service including full and partial dentures, laminated mouth guards, and bite splints. We understand the needs of dentists and look to provide work that arrives back at your surgery ahead of time, fits without time consuming and frustrating adjustments, and looks good in the mouth.</p>
  </div>

  <h2 class="section-title panel-title" style="left:445px; top:760px;">How To Deliver Better<br>Partial Dentures:</h2>
  <div class="copy panel-copy" style="left:445px; top:817px; width:339px;">
    <p>Dentistry is changing day by day. The latest innovative denture materials and techniques allow dentists to prescribe partial dentures that are more aesthetic, function better, and enhance the patient experience. If you are looking to deliver the very best partial dentures utilising these new materials, BrightMold has the solution.</p>
  </div>

  <div class="footer-divider"></div>

  <div class="brand">BrightMold</div>

  <ul class="contact">
    <li class="contact-name">
      <svg viewBox="0 0 20 20"><circle cx="10" cy="10" r="9" fill="none" stroke="#1d1d1d" stroke-width="2"/><circle cx="10" cy="8" r="3.3" fill="#1d1d1d"/><path d="M4.5 16 C6 12 14 12 15.5 16" fill="#1d1d1d"/></svg>
      Darren Whitcombe
    </li>
    <li>
      <svg viewBox="0 0 20 20"><path d="M2 7 C2 3 18 3 18 7 L15 8 L14 6 H6 L5 8 Z" fill="#1d1d1d"/><rect x="4" y="9" width="12" height="8" rx="1.5" fill="#1d1d1d"/><circle cx="10" cy="13" r="2" fill="#fff"/></svg>
      09 555 0182
    </li>
    <li>
      <svg viewBox="0 0 20 20"><path d="M2 7 C2 3 18 3 18 7 L15 8 L14 6 H6 L5 8 Z" fill="#1d1d1d"/><rect x="4" y="9" width="12" height="8" rx="1.5" fill="#1d1d1d"/><circle cx="10" cy="13" r="2" fill="#fff"/></svg>
      021 555 0347
    </li>
    <li>
      <svg viewBox="0 0 20 20"><path d="M10 2 C6 2 4 5 4 8 C4 12 10 18 10 18 C10 18 16 12 16 8 C16 5 14 2 10 2 Z" fill="#1d1d1d"/><circle cx="10" cy="8" r="2.4" fill="#fff"/></svg>
      412 Kowhai Ridge Rd, RD2, Tauranga 3172
    </li>
    <li>
      <svg viewBox="0 0 20 20"><rect x="3" y="5" width="14" height="11" fill="none" stroke="#1d1d1d" stroke-width="1.6"/><path d="M3 5 L10 11 L17 5" fill="none" stroke="#1d1d1d" stroke-width="1.6"/></svg>
      darrenwhitcombe@mailbox.co.nz
    </li>
  </ul>

  <div class="base-rule"></div>
  <div class="base-band"></div>
</main>
</body>
</html>
```